Atelier Solvane est le nom pour lancer une nouvelle activité dans la Décoration
Besoins
Je souhaite quelque chose qui reflète le luxe, l'élégance et la sobriété mais surtout pas quelque chose de cucu romantique mais plutôt cocooning, moderne, design
Description de l'entreprise
Entreprise de décoration d'intérieur situé dans les Alpes près de la Suisse. Conseils, mise en relation avec des artisans, prospection commercial pour le client...
La cible
Cible haut de gamme, probablement beaucoup de chalets.
Couleurs, favoris et autres exigences:
Pas de couleurs jaune, saumon, rouge et de rose.
Plus dans des contrastes de couleurs et non des couleurs pastels
Une belle typo modern et design

```html
<!DOCTYPE html>
<html lang="fr">
<head>
<meta charset="utf-8">
<title>Atelier Solvane – Papeterie</title>
<link rel="stylesheet" href="https://fonts.googleapis.com/css2?family=Open+Sans:wght@300;400&family=Arimo:wght@400;700&display=swap">
<style>
  :root {
    --plum: #3d1f4f;
    --silver: #b3b1b6;
    --ink: #1a1a1a;
    --mute: #8c8a90;
    --paper: #ffffff;
    --ground: #ffffff;
    --edge: #e2e1e4;
  }
  * { box-sizing: border-box; margin: 0; padding: 0; }
  html, body { width: 1200px; height: 1200px; overflow: hidden; background: var(--ground); }
  body { position: relative; font-family: "Arimo", Arial, sans-serif; color: var(--ink); }

  .sheet { position: absolute; background: var(--paper); border: 1px solid var(--edge); box-shadow: 0 3px 10px rgba(0,0,0,.12); overflow: hidden; }

  .brand { position: absolute; display: flex; flex-direction: column; align-items: flex-start; }
  .brand-row { display: flex; align-items: center; gap: 10px; }
  .brand-dot { width: 14px; height: 14px; border-radius: 50%; background: var(--plum); flex: none; }
  .brand-name { font-family: "Open Sans", Arial, sans-serif; font-weight: 300; color: var(--plum); white-space: nowrap; }
  .brand-tagline { font-family: "Open Sans", Arial, sans-serif; font-weight: 300; color: var(--mute); letter-spacing: 2px; margin-top: 2px; white-space: nowrap; }

  .band { position: absolute; top: 0; bottom: 0; background: var(--plum); }
  .band-rule { position: absolute; top: 0; bottom: 0; background: var(--silver); }
  .vertical-url { position: absolute; writing-mode: vertical-rl; transform: rotate(180deg); color: #fff; white-space: nowrap; }

  .faint-name { position: absolute; font-family: "Open Sans", Arial, sans-serif; font-weight: 300; white-space: nowrap; }

  /* letterhead */
  .letterhead { left: 24px; top: 20px; width: 616px; height: 880px; }
  .letterhead .band { left: 0; width: 44px; }
  .letterhead .band-rule { left: 44px; width: 12px; }
  .letterhead .vertical-url { left: 10px; bottom: 14px; font-size: 24px; }
  .letterhead .brand { left: 76px; top: 150px; }
  .letterhead .brand-name { font-size: 26px; }
  .letterhead .brand-tagline { font-size: 8px; margin-left: 24px; }
  .sender-block { position: absolute; right: 14px; top: 30px; width: 200px; text-align: right; font-size: 11px; line-height: 14px; font-style: normal; }
  .letter-title { position: absolute; left: 56px; right: 0; top: 240px; text-align: center; font-size: 15px; font-weight: 400; }
  .letter-body { position: absolute; left: 106px; right: 8px; top: 285px; font-size: 11px; line-height: 14px; }
  .letter-body p { margin-bottom: 14px; }
  .letterhead .faint-name { left: 110px; top: 790px; font-size: 40px; color: rgba(61,31,79,.06); }
  .signature { position: absolute; left: 380px; top: 720px; width: 120px; height: 40px; border-radius: 20px; background: linear-gradient(90deg, rgba(26,26,26,.10), rgba(26,26,26,.03)); }

  /* envelope */
  .envelope { left: 575px; top: 200px; width: 585px; height: 300px; z-index: 2; }
  .envelope .band-rule { left: 385px; width: 18px; }
  .envelope .band { left: 403px; right: 0; }
  .envelope .vertical-url { left: 408px; top: 16px; font-size: 22px; }
  .envelope .faint-name { right: 14px; top: 140px; font-size: 15px; color: rgba(255,255,255,.14); }
  .envelope .brand { left: 120px; top: 150px; }
  .envelope .brand-name { font-size: 24px; }
  .envelope .brand-tagline { font-size: 8px; margin-left: 24px; }

  /* business card front */
  .card-front { left: 572px; top: 570px; width: 298px; height: 172px; z-index: 2; }
  .card-front .brand { left: 66px; top: 92px; }
  .card-front .brand-name { font-size: 17px; }
  .card-front .brand-dot { width: 10px; height: 10px; }
  .card-front .brand-tagline { font-size: 6px; margin-left: 20px; letter-spacing: 1.5px; }

  /* business card back */
  .card-back { left: 880px; top: 570px; width: 290px; height: 172px; z-index: 2; }
  .card-back .band-rule { left: 186px; width: 14px; }
  .card-back .band { left: 200px; right: 0; }
  .card-back .vertical-url { left: 204px; top: 10px; font-size: 13px; }
  .card-back .faint-name { right: 6px; top: 80px; font-size: 8px; color: rgba(255,255,255,.16); }
  .contact { position: absolute; left: 10px; top: 18px; }
  .contact-name { font-family: "Open Sans", Arial, sans-serif; font-size: 18px; color: var(--plum); }
  .contact-phone { font-size: 12px; color: var(--mute); margin-top: 6px; letter-spacing: .5px; }
  .contact-company { font-size: 13px; color: var(--plum); margin-top: 18px; }
  .contact-city { font-size: 13px; color: var(--plum); font-weight: 700; margin-top: 2px; }
  .contact-email { font-size: 8px; color: var(--mute); margin-top: 26px; }

  /* web start page */
  .web-tile { left: 762px; top: 852px; width: 292px; height: 186px; }
  .web-tile .brand { left: 58px; top: 90px; }
  .web-tile .brand-name { font-size: 19px; }
  .web-tile .brand-dot { width: 11px; height: 11px; }
  .web-tile .brand-tagline { font-size: 6px; margin-left: 21px; letter-spacing: 1.5px; }
</style>
</head>
<body>

<section class="sheet letterhead" aria-label="Papier à en-tête">
  <div class="band"></div>
  <div class="band-rule"></div>
  <div class="vertical-url">www.atelier-solvane.com</div>
  <div class="faint-name" aria-hidden="true">Atelier Solvane</div>

  <div class="brand">
    <div class="brand-row"><span class="brand-dot"></span><span class="brand-name">Atelier Solvane</span></div>
    <span class="brand-tagline">Décoration d'intérieur</span>
  </div>

  <address class="sender-block">
    Lorem ipsum dolor sit amet,<br>consectetur<br>adipiscing elit.<br>Sed non risus. mi d mi, non<br>fermentum diam nisl sit<br>amet erat
  </address>

  <h1 class="letter-title">Lorem ipsum dolor sit</h1>

  <div class="letter-body">
    <p>Lorem ipsum dolor sit amet, consectetur adipiscing elit. Sed non risus. Suspendisse lectus tortor, dignissim sit amet, adipiscing nec, ultricies sed, dolor. Cras elementum ultrices diam. Maecenas ligula massa, varius a, semper congue, euismod non, mi. Proin porttitor, orci nec nonummy molestie, enim est eleifend mi, non fermentum diam nisl sit amet erat</p>
    <p>. Duis semper. Duis arcu massa, scelerisque vitae, consequat in, pretium a, enim. Pellentesque congue. Ut in risus volutpat libero pharetra tempor. Cras vestibulum bibendum augue. Praesent egestas leo in pede. Praesent blandit odio eu enim. Pellentesque sed dui ut augue blandit sodales. Vestibulum ante ipsum primis in faucibus orci luctus et ultrices posuere cubilia Curae; Aliquam nibh. Mauris ac mauris sed pede pellentesque fermentum</p>
    <p>. Maecenas adipiscing ante non diam sodales hendrerit. Ut velit mauris, egestas sed, gravida nec, ornare ut, mi. Aenean ut orci vel massa suscipit pulvinar. Nulla sollicitudin. Fusce varius, ligula non tempus aliquam, nunc turpis ullamcorper nibh,</p>
    <p>in tempus sapien eros vitae ligula. Pellentesque rhoncus nunc et augue. Integer id felis. Curabitur aliquet pellentesque diam. Integer quis metus vitae elit lobortis egestas. Lorem ipsum dolor sit amet, consectetuer adipiscing elit. Morbi vel erat non mauris convallis vehicula. Nulla et sapien. Integer tortor tellus, aliquam faucibus, convallis id, congue eu, quam. Mauris ullamcorper felis vitae erat. Proin feugiat, augue non elementum posuere, metus purus iaculis lectus, et tristique ligula justo vitae magna.</p>
  </div>

  <div class="signature" role="img" aria-label="Signature manuscrite"></div>
</section>

<section class="sheet envelope" aria-label="Enveloppe">
  <div class="band-rule"></div>
  <div class="band"></div>
  <div class="vertical-url">www.atelier-solvane.com</div>
  <div class="faint-name" aria-hidden="true">Atelier Solvane</div>
  <div class="brand">
    <div class="brand-row"><span class="brand-dot"></span><span class="brand-name">Atelier Solvane</span></div>
    <span class="brand-tagline">Décoration d'intérieur</span>
  </div>
</section>

<section class="sheet card-front" aria-label="Carte de visite, recto">
  <div class="brand">
    <div class="brand-row"><span class="brand-dot"></span><span class="brand-name">Atelier Solvane</span></div>
    <span class="brand-tagline">Décoration d'intérieur</span>
  </div>
</section>

<section class="sheet card-back" aria-label="Carte de visite, verso">
  <div class="contact">
    <div class="contact-name">Name Firstname</div>
    <div class="contact-phone">+33 12 34 56 78</div>
    <div class="contact-company">company address</div>
    <div class="contact-city">12345 - City</div>
    <div class="contact-email">contact@atelier-solvane.com</div>
  </div>
  <div class="band-rule"></div>
  <div class="band"></div>
  <div class="vertical-url">www.atelier-solvane.com</div>
  <div class="faint-name" aria-hidden="true">Atelier Solvane</div>
</section>

<section class="sheet web-tile" aria-label="Page d'accueil du site">
  <div class="brand">
    <div class="brand-row"><span class="brand-dot"></span><span class="brand-name">Atelier Solvane</span></div>
    <span class="brand-tagline">Décoration d'intérieur</span>
  </div>
</section>

</body>
</html>
```